Luxury Caviar Tin Label for High End Caviar Retailer

We are looking for a new caviar label design. We want something unique, preferably black and gold or dark blue and gold. We want a modern and luxurious feel. We have several types of caviar so we need to be able to change the name of the caviar when we print the labels. See inspiration attached. Logo is also attached. More about us: kvmarlune.com

Industry/Entity Type

fine foods industry, caviar

Font styles to use
Serif
Decorative

Requirements
Must have
• KV Marlune Logo, space for caviar name
Nice to have
• black and gold, blue and gold

```html
<!DOCTYPE html>
<html lang="en">
<head>
<meta charset="utf-8">
<title>KV Marlune – Caviar Tin Labels</title>
<link rel="stylesheet" href="https://fonts.googleapis.com/css2?family=Cinzel:wght@600;700&family=Marcellus&family=Pinyon+Script&display=swap">
<style>
  :root {
    --paper: #ffffff;
    --tin-black: #020202;
    --gold: #d9b16a;
    --gold-light: #f3dc9e;
    --gold-deep: #a8742f;
  }
  html, body {
    margin: 0;
    padding: 0;
    width: 1200px;
    height: 593px;
    overflow: hidden;
    background: var(--paper);
  }
  .label-sheet {
    display: block;
    width: 1200px;
    height: 593px;
  }
  .tin-face { fill: var(--tin-black); }
  .dotted-ring {
    fill: none;
    stroke: var(--gold);
    stroke-width: 2.2;
    stroke-dasharray: 0 5.2;
    stroke-linecap: round;
  }
  .fine-ring {
    fill: none;
    stroke: var(--gold-deep);
    stroke-width: 0.8;
  }
  .brand-name {
    font-family: "Marcellus", serif;
    font-size: 42px;
    fill: var(--gold);
    text-anchor: middle;
    letter-spacing: 0.5px;
  }
  .tagline {
    font-family: "Pinyon Script", cursive;
    font-size: 30px;
    fill: var(--gold);
    text-anchor: middle;
  }
  .divider {
    stroke: var(--gold);
    stroke-width: 0.9;
  }
  .caviar-variety {
    font-family: "Cinzel", serif;
    font-weight: 600;
    font-size: 15px;
    fill: var(--gold);
    text-anchor: middle;
    letter-spacing: 4.4px;
  }
  .product-type {
    font-family: "Cinzel", serif;
    font-weight: 700;
    font-size: 31px;
    fill: var(--gold-light);
    text-anchor: middle;
    letter-spacing: 3px;
  }
</style>
</head>
<body>
<svg class="label-sheet" viewBox="0 0 1200 593" xmlns="http://www.w3.org/2000/svg">
  <defs>
    <linearGradient id="crest-tone" x1="0" y1="0" x2="1" y2="1">
      <stop offset="0" stop-color="#f0d597"/>
      <stop offset="0.55" stop-color="#c99a50"/>
      <stop offset="1" stop-color="#8d5f26"/>
    </linearGradient>
  </defs>

  <g class="tin-label" transform="translate(324 297)">
    <circle class="tin-face" r="258"/>
    <circle class="fine-ring" cx="2" cy="0" r="243"/>
    <circle class="dotted-ring" r="238"/>
    <rect class="crest-artwork" role="img" aria-label="Gold heraldic crest with shield and scrolling foliage" x="-162" y="-170" width="323" height="161" rx="40" fill="url(#crest-tone)" opacity="0.9"/>
    <text class="brand-name" x="0" y="40">KV MARLUNE</text>
    <text class="tagline" x="0" y="73">Premium Quality</text>
    <line class="divider" x1="-53" y1="92" x2="70" y2="92"/>
    <text class="caviar-variety" x="4" y="116">OSETRA IMPERIAL GOLD</text>
    <text class="product-type" x="4" y="152">·CAVIAR·</text>
    <rect class="flourish" role="img" aria-label="Small gold floral flourish" x="-16" y="170" width="44" height="22" rx="11" fill="url(#crest-tone)"/>
  </g>

  <g class="tin-label" transform="translate(890 297)">
    <circle class="tin-face" r="258"/>
    <circle class="fine-ring" cx="2" cy="0" r="243"/>
    <circle class="dotted-ring" r="238"/>
    <rect class="crest-artwork" role="img" aria-label="Gold heraldic crest with shield and scrolling foliage" x="-162" y="-170" width="323" height="161" rx="40" fill="url(#crest-tone)" opacity="0.9"/>
    <text class="brand-name" x="0" y="40">KV MARLUNE</text>
    <text class="tagline" x="0" y="73">Premium Quality</text>
    <line class="divider" x1="-53" y1="92" x2="70" y2="92"/>
    <text class="caviar-variety" x="4" y="116">OSETRA IMPERIAL GOLD</text>
    <text class="product-type" x="4" y="152">·CAVIAR·</text>
    <rect class="flourish" role="img" aria-label="Small gold floral flourish" x="-16" y="170" width="44" height="22" rx="11" fill="url(#crest-tone)"/>
  </g>
</svg>
</body>
</html>
```